Tessa Brangle Consulting

I am starting my own business and want to have a business card that stands out from the rest. Class is the word i use to describe what i would like to my card to look like.

I see my card as vibrant red card with rounded edges. mat finish
Centered scripted writing
large scripted font: Tessa Brangle, smaller font & not scripted: Consulting, next line 0498173226, next line tessa@branglehome.com.au

i have now left 2 email message for the design of my card. Family is spelt wrong on the card. this needs to be correct and finial proof sent though!!! before i can download and approve
Tessa

Target Market(s)

Real Estate Professionals

Industry/Entity Type

Business

Contact Information for Business Card

Tessa Brangle
Consulting
0498 173 226
tessa@branglehouse.com.au

Logo Text

no logo

Requirements
Must have
• must have rounded edges

```html
<!DOCTYPE html>
<html lang="en">
<head>
<meta charset="utf-8">
<title>Tessa Brangle Consulting – Business Card</title>
<link rel="stylesheet" href="https://fonts.googleapis.com/css2?family=Pinyon+Script&family=Cormorant+Garamond:wght@600&family=Questrial&display=swap">
<style>
  :root {
    --backdrop: #2a211c;
    --card-red-light: #a81e24;
    --card-red-mid: #921a1f;
    --card-red-dark: #6e1216;
    --ink: #0d0506;
    --silver: #e9e4e2;
    --silver-shade: #b9b2b0;
  }
  * { margin: 0; padding: 0; box-sizing: border-box; }
  html, body {
    width: 1200px;
    height: 900px;
    overflow: hidden;
    background: var(--backdrop);
  }
  .canvas {
    position: relative;
    width: 1200px;
    height: 900px;
  }
  .business-card {
    position: absolute;
    left: 180px;
    top: 195px;
    width: 840px;
    height: 510px;
    border-radius: 34px;
    background: linear-gradient(160deg, var(--card-red-light) 0%, var(--card-red-mid) 55%, var(--card-red-dark) 100%);
    box-shadow: 0 14px 30px rgba(0, 0, 0, 0.45);
    text-align: center;
    padding-left: 60px;
  }
  .card-name {
    font-family: "Pinyon Script", cursive;
    font-weight: 400;
    font-size: 104px;
    line-height: 1;
    color: var(--ink);
    margin-top: 120px;
  }
  .card-tagline {
    font-family: "Cormorant Garamond", serif;
    font-weight: 600;
    font-size: 34px;
    letter-spacing: 2px;
    font-variant: small-caps;
    text-transform: lowercase;
    background: linear-gradient(180deg, var(--silver) 40%, var(--silver-shade) 100%);
    -webkit-background-clip: text;
    background-clip: text;
    color: transparent;
    margin-top: 8px;
  }
  .card-contact {
    font-family: "Questrial", sans-serif;
    color: var(--ink);
    font-size: 25px;
    letter-spacing: 2px;
    line-height: 1.9;
    margin-top: 62px;
  }
</style>
</head>
<body>
  <main class="canvas">
    <section class="business-card">
      <h1 class="card-name">Tessa Brangle</h1>
      <p class="card-tagline">Consulting</p>
      <div class="card-contact">
        <p class="card-phone">0498 173 226</p>
        <p class="card-email">tessa@branglehouse.com.au</p>
      </div>
    </section>
  </main>
</body>
</html>
```